Major infrastructure project needs a diagram designed

We need two simple diagrams created on Sydney's current (1) and future (2) intermodal terminal capacity and the number of shipping containers coming out of Kellmere Dock.

Please see attached file for full instructions (Word and PDF attached)

```html
<!DOCTYPE html>
<html lang="en">
<head>
<meta charset="utf-8">
<title>Intermodal terminal capacity</title>
<link rel="stylesheet" href="https://fonts.googleapis.com/css2?family=Open+Sans:wght@400;600;700&display=swap">
<style>
:root{
  --teal:#1798a8;
  --ink:#2b3440;
  --panel:#e9e9ea;
  --imex:#f7b12c;
  --imex-light:#fbd27a;
  --inter:#3b4756;
  --inter-light:#5a6878;
  --empty:#bdbec0;
  --empty-light:#d9dadb;
  --rule:#3a4350;
}
*{box-sizing:border-box;margin:0;padding:0}
html,body{width:1200px;height:848px;overflow:hidden;background:#fff}
body{position:relative;font-family:"Open Sans",Arial,sans-serif;color:var(--ink)}
.abs{position:absolute}

.section-title{position:absolute;font-size:15px;font-weight:700;color:var(--ink);white-space:nowrap;transform:translateX(-50%)}
.section-title .accent{color:var(--teal)}
.title-rule{position:absolute;height:2px;background:var(--teal)}

.panel{position:absolute;background:var(--panel);top:148px;height:359px;border-bottom:2px solid var(--rule)}
.axis{position:absolute;top:146px;height:8px;border-top:2px solid var(--rule);
  background:repeating-linear-gradient(90deg,var(--rule) 0 1px,transparent 1px 9.4px)}
.axis-label{position:absolute;top:128px;font-size:10px;font-weight:700;transform:translateX(-50%);white-space:nowrap}
.unit{position:absolute;font-size:10px;font-weight:700;line-height:11px;text-align:center}

.terminals{position:absolute;left:530px;top:45px;width:126px;height:660px;background:var(--teal);border-radius:5px;overflow:hidden}
.terminals-head{position:absolute;top:22px;width:100%;text-align:center;color:#fff;font-weight:700;font-size:14px}
.terminal{position:absolute;width:100%;text-align:center;color:#fff;font-size:11.5px;line-height:13px;transform:translateY(-50%)}
.terminal small{display:block;font-style:italic;font-size:10px}
.crane-art{position:absolute;left:0;top:520px;width:126px;height:140px;
  background:linear-gradient(180deg,rgba(40,70,85,.15),rgba(30,70,85,.55))}

.value{position:absolute;font-size:11px;font-weight:700;transform:translateY(-50%);white-space:nowrap}
.bar{position:absolute;height:21px;transform:translateY(-50%)}
.bar.imex{background:
  repeating-linear-gradient(90deg,transparent 0 47px,#fff 47px 49px),
  repeating-linear-gradient(90deg,var(--imex) 0 2px,var(--imex-light) 2px 3px)}
.bar.inter{background:
  repeating-linear-gradient(90deg,transparent 0 47px,#fff 47px 49px),
  repeating-linear-gradient(90deg,var(--inter) 0 2px,var(--inter-light) 2px 3px)}
.bar.empty{background:
  repeating-linear-gradient(90deg,transparent 0 47px,#fff 47px 49px),
  repeating-linear-gradient(90deg,var(--empty) 0 2px,var(--empty-light) 2px 3px)}
.left .bar{background-position:right}
.pending{position:absolute;left:660px;top:291px;width:400px;height:20px;
  background:linear-gradient(90deg,rgba(200,200,202,0),#d3d3d5 40%,#d3d3d5 60%,rgba(200,200,202,0));
  font-size:9px;font-weight:700;text-align:center;line-height:20px;padding-left:40px}
.more{position:absolute;font-size:11px;font-weight:700}

.band{position:absolute;top:580px;height:26px;background:var(--panel);font-size:12px;font-weight:700;text-align:center;line-height:26px}
.mode{position:absolute;top:624px;font-size:12px;font-weight:700;transform:translateX(-50%);white-space:nowrap}
.mode span{font-weight:400}
.icon{position:absolute;top:650px;height:40px;background:var(--ink);border-radius:4px;opacity:.85}
.divider{position:absolute;top:624px;width:1px;height:56px;background:#9aa0a6}

.legend{position:absolute;left:56px;top:745px;width:1077px;height:56px;border:1px solid #8c9096;border-radius:8px}
.key{position:absolute;height:16px;width:47px;top:765px}
.key-label{position:absolute;font-size:10px;font-weight:700;line-height:11px}
</style>
</head>
<body>

<!-- Current capacity -->
<div class="title-rule" style="left:55px;top:75px;width:150px"></div>
<div class="title-rule" style="left:378px;top:75px;width:149px"></div>
<div class="section-title" style="left:292px;top:65px"><span class="accent">CURRENT</span> capacity</div>

<div class="axis-label" style="left:55px">200,000</div>
<div class="axis-label" style="left:150px">150,000</div>
<div class="axis-label" style="left:245px">100,000</div>
<div class="axis-label" style="left:340px">50,000</div>
<div class="axis-label" style="left:432px">0</div>
<div class="unit" style="left:470px;top:118px">TEUs/<br>annum</div>
<div class="panel" style="left:55px;width:472px"></div>
<div class="axis" style="left:55px;width:378px"></div>

<div class="left">
  <div class="bar inter" style="left:226px;width:102px;top:328px"></div>
  <div class="bar imex" style="left:328px;width:104px;top:328px"></div>
  <div class="bar imex" style="left:394px;width:38px;top:357px"></div>
  <div class="bar imex" style="left:149px;width:283px;top:387px"></div>
  <div class="bar inter" style="left:55px;width:377px;top:416px"></div>
  <div class="bar empty" style="left:149px;width:283px;top:446px"></div>
  <div class="bar imex" style="left:338px;width:94px;top:475px"></div>
</div>
<div class="value" style="left:466px;top:328px">110,000</div>
<div class="value" style="left:474px;top:357px">20,000</div>
<div class="value" style="left:466px;top:387px">150,000</div>
<div class="value" style="left:466px;top:416px">200,000</div>
<div class="value" style="left:466px;top:446px">150,000</div>
<div class="value" style="left:474px;top:475px">50,000</div>

<!-- Proposed capacity -->
<div class="title-rule" style="left:660px;top:75px;width:150px"></div>
<div class="title-rule" style="left:982px;top:75px;width:151px"></div>
<div class="section-title" style="left:896px;top:65px"><span class="accent">PROPOSED</span> capacity</div>

<div class="unit" style="left:692px;top:118px">TEUs/<br>annum</div>
<div class="axis-label" style="left:754px">0</div>
<div class="axis-label" style="left:848px">250,000</div>
<div class="axis-label" style="left:944px">500,000</div>
<div class="axis-label" style="left:1098px;transform:none;left:1075px">1million ...</div>
<div class="panel" style="left:660px;width:473px"></div>
<div class="axis" style="left:754px;width:379px"></div>

<div class="value" style="left:672px;top:172px">1,600 000</div>
<div class="value" style="left:680px;top:214px">500,000</div>
<div class="value" style="left:688px;top:242px">70,000</div>
<div class="value" style="left:688px;top:270px">50,000</div>
<div class="value" style="left:680px;top:328px">160,000</div>
<div class="value" style="left:688px;top:357px">50,000</div>
<div class="value" style="left:680px;top:387px">200,000</div>
<div class="value" style="left:680px;top:416px">350,000</div>
<div class="value" style="left:680px;top:446px">150,000</div>
<div class="value" style="left:680px;top:475px">300,000</div>

<div class="bar imex" style="left:754px;width:194px;top:172px"></div>
<div class="bar inter" style="left:948px;width:194px;top:172px"></div>
<div class="more" style="left:1146px;top:162px">...</div>
<div class="bar imex" style="left:754px;width:95px;top:214px"></div>
<div class="bar inter" style="left:849px;width:94px;top:214px"></div>
<div class="bar imex" style="left:754px;width:26px;top:242px"></div>
<div class="bar imex" style="left:754px;width:12px;top:270px"></div>
<div class="bar inter" style="left:766px;width:8px;top:270px"></div>
<div class="pending">still to investigate</div>
<div class="bar imex" style="left:754px;width:32px;top:328px"></div>
<div class="bar inter" style="left:786px;width:29px;top:328px"></div>
<div class="bar imex" style="left:754px;width:19px;top:357px"></div>
<div class="bar imex" style="left:754px;width:75px;top:387px"></div>
<div class="bar inter" style="left:754px;width:132px;top:416px"></div>
<div class="bar empty" style="left:754px;width:57px;top:446px"></div>
<div class="bar imex" style="left:754px;width:113px;top:475px"></div>

<!-- Terminals column -->
<div class="terminals">
  <div class="terminals-head">TERMINALS</div>
  <div class="terminal" style="top:134px">MOOREBANK<small>(Ravena 1,000 000)</small></div>
  <div class="terminal" style="top:169px">EASTERN CREEK</div>
  <div class="terminal" style="top:197px">INGLEBURN</div>
  <div class="terminal" style="top:225px">LEUMEAH</div>
  <div class="terminal" style="top:255px">BADGERYS CREEK</div>
  <div class="terminal" style="top:283px">YENNORA</div>
  <div class="terminal" style="top:312px">VILLAWOOD</div>
  <div class="terminal" style="top:342px">MINTO</div>
  <div class="terminal" style="top:371px">CHULLORA</div>
  <div class="terminal" style="top:401px">COOKS RIVER,<br>ST PETERS</div>
  <div class="terminal" style="top:429px">ENFIELD</div>
  <div class="crane-art" role="img" aria-label="Container cranes at the dock"></div>
</div>

<!-- Distribution -->
<div class="title-rule" style="left:55px;top:564px;width:122px"></div>
<div class="title-rule" style="left:408px;top:564px;width:119px"></div>
<div class="section-title" style="left:292px;top:554px"><span class="accent">Kellmere</span> DOCK distribution</div>
<div class="band" style="left:56px;width:471px">2 million TEUs/annum</div>
<div class="mode" style="left:175px">300,000 by rail <span>(15%)</span></div>
<div class="mode" style="left:411px">1.7 million by road <span>(85%)</span></div>
<div class="divider" style="left:291px"></div>
<div class="icon" style="left:160px;width:28px" role="img" aria-label="Train icon"></div>
<div class="icon" style="left:380px;width:60px;height:30px;top:655px" role="img" aria-label="Truck icon"></div>

<div class="title-rule" style="left:660px;top:564px;width:122px"></div>
<div class="title-rule" style="left:1012px;top:564px;width:121px"></div>
<div class="section-title" style="left:896px;top:554px"><span class="accent">Kellmere</span> DOCK distribution</div>
<div class="band" style="left:660px;width:473px">7 million TEUs/annum</div>
<div class="mode" style="left:782px">3 million by rail <span>(43%)</span></div>
<div class="mode" style="left:1015px">4 million by road <span>(57%)</span></div>
<div class="divider" style="left:898px"></div>
<div class="icon" style="left:767px;width:28px" role="img" aria-label="Train icon"></div>
<div class="icon" style="left:985px;width:60px;height:30px;top:655px" role="img" aria-label="Truck icon"></div>

<!-- Legend -->
<div class="legend"></div>
<div class="key bar imex" style="left:270px;top:773px"></div>
<div class="key-label" style="left:329px;top:764px">IMEX (import-export)<br>Terminal</div>
<div class="key bar inter" style="left:506px;top:773px"></div>
<div class="key-label" style="left:564px;top:770px">Interstate Terminal</div>
<div class="key bar empty" style="left:723px;top:773px"></div>
<div class="key-label" style="left:783px;top:768px">Storage Empty Containers</div>

</body>
</html>
```